Brookvale Systems Yellow rose letterhead

I have a new logo for my company but in its current form it is too large to be used on letterhead or as a email signature. I need to have the designer use elements from the current logo and create something close to the original but more suited for smaller items.
Updates

I just uploaded a copy of our logo that does not have the weathered affect. Thanks

Industry/Entity Type

It Company

Requirements
Must have
• The design must maintain the visual effect of the current logo. It needs to include the yellow rose and the name of the company.
Nice to have
• It would be nice to maintain the stamp theme and incorporate my name, address, phone, email. etc.

```html
<!DOCTYPE html>
<html lang="en">
<head>
<meta charset="utf-8">
<title>Brookvale Systems Letterhead</title>
<link href="https://fonts.googleapis.com/css2?family=Gelasio:wght@400;700&family=Nunito+Sans:wght@400;700&display=swap" rel="stylesheet">
<style>
  :root {
    --backdrop: #e8e5e0;
    --paper: #ffffff;
    --ink: #222222;
    --stamp-dark: #4a4240;
    --stamp-orange: #f0a23a;
    --stamp-orange-deep: #d9791f;
    --rose-yellow: #f7c948;
    --rose-gold: #e99a2a;
    --teal: #2fb3b9;
    --cream: #f4efe6;
  }
  * { box-sizing: border-box; margin: 0; padding: 0; }
  html, body { width: 1200px; height: 1200px; overflow: hidden; }
  body { background: var(--backdrop); position: relative; font-family: "Gelasio", Georgia, serif; color: var(--ink); }

  .letter-page {
    position: absolute; left: 136px; top: 0;
    width: 928px; height: 1200px;
    background: var(--paper);
    padding: 56px 80px 0 80px;
    box-shadow: 0 0 18px rgba(0,0,0,0.12);
  }

  .letterhead-stamp {
    width: 340px; height: 230px;
    background: var(--stamp-orange);
    border: 3px solid var(--stamp-orange-deep);
    padding: 14px;
  }
  .stamp-panel {
    position: relative; width: 100%; height: 100%;
    background: var(--stamp-dark);
    padding: 14px 16px 12px 16px;
    color: var(--cream);
    font-family: "Nunito Sans", Arial, sans-serif;
  }
  .rose-art {
    position: absolute; left: 10px; top: 10px;
    width: 96px; height: 88px;
    border-radius: 50%;
    background: radial-gradient(circle at 45% 45%, var(--rose-yellow), var(--rose-gold) 80%);
  }
  .company-name {
    text-align: right;
    font-size: 26px; font-weight: 700; line-height: 1.05;
    color: var(--cream);
  }
  .contact-block {
    text-align: right; margin-top: 22px;
    font-size: 13px; line-height: 1.22; font-style: normal;
  }
  .contact-block .accent { color: var(--teal); }

  .letter-body { margin-top: 44px; font-size: 16px; line-height: 1.5; width: 700px; }
  .letter-body p { margin-bottom: 22px; }
  .letter-body h2 { font-size: 17px; font-weight: 700; margin-bottom: 4px; }
  .letter-body ul { list-style: none; margin-bottom: 22px; }
  .letter-body li::before { content: "• "; }
  .signoff { margin-top: 8px; }
  .signature-lines { margin-top: 30px; line-height: 1.4; }
</style>
</head>
<body>
  <main class="letter-page">
    <header class="letterhead-stamp">
      <div class="stamp-panel">
        <div class="rose-art" role="img" aria-label="Illustration of a yellow rose with teal leaves"></div>
        <div class="company-name">Brookvale<br>Systems</div>
        <address class="contact-block">
          Nora Whitfield, PhD<br>
          214 Harlow Ridge Road, Ste 118<br>
          Millbrook, TX 75902<br>
          <span class="accent">nora@brookvale-systems.example</span><br>
          <span class="accent">1.800.555.0142</span>
        </address>
      </div>
    </header>

    <section class="letter-body">
      <p>Salutation:</p>
      <p>This is not real copy. This is Greek. And nobody’s supposed to be able to understand Greek. Hence the phrase, “Hey, man, it’s all Greek to me” which means “I don’t understand it.” So if you’re reading along, and you notice that this copy isn’t making any sense, that’s perfectly alright. Because it’s not important that you get the meaning of the copy. After all, it’s Greek. And nobody’s supposed to be able to understand Greek. Hence the phrase, “Hey, man, it’s all Greek.”</p>
      <h2>This is not real copy</h2>
      <p>This is Greek. And nobody’s supposed to be able to understand Greek. Hence the phrase, “Hey, man, it’s all Greek to me” which means “I don’t understand it.” So if you’re reading along, and you notice that this copy isn’t making any sense, that’s perfectly alright. Because it’s not important that you get the meaning of the copy. After all, it’s Greek. And nobody’s supposed to be able to understand Greek. Hence the phrase, “Hey, man, it’s all Greek.” This is not real copy. This is Greek. And nobody’s supposed to be able to understand Greek.</p>
      <ul>
        <li>After all, it’s Greek. And nobody’s supposed to be able to understand Greek.</li>
        <li>Hence the phrase, “Hey, man, it’s all Greek.”</li>
        <li>This is not real copy. This is Greek.</li>
      </ul>
      <p>And nobody’s supposed to be able to understand Greek. Hence the phrase, “Hey, man, it’s all Greek to me” which means “I don’t understand it.” So if you’re reading along, and you notice that this copy isn’t making any sense, that’s perfectly alright.</p>
      <p>Because it’s not important that you get the meaning of the copy. After all, it’s Greek. And nobody’s supposed to be able to understand Greek. Hence the phrase.</p>
      <p class="signoff">Sincerely,</p>
      <p class="signature-lines">Name<br>Title</p>
    </section>
  </main>
</body>
</html>
```